Business Cards for 4 people

We need to update our current business cards for 4 of our employees and make some minor design changes. Mostly have to update the information on the cards with a new address and titles.

```html
<!DOCTYPE html>
<html lang="en">
<head>
<meta charset="utf-8">
<title>Ledgerline Partners – Business Card</title>
<link href="https://fonts.googleapis.com/css2?family=Poppins:wght@300;400;600;700&display=swap" rel="stylesheet">
<style>
  :root {
    --navy: #21315f;
    --green: #008f3e;
    --white: #ffffff;
    --ink: #3a3a3a;
    --backdrop: #ececec;
  }
  * { box-sizing: border-box; margin: 0; padding: 0; }
  html, body { width: 1200px; height: 1200px; overflow: hidden; }
  body {
    background: var(--backdrop);
    font-family: "Poppins", sans-serif;
    position: relative;
  }
  .card {
    position: absolute;
    left: 150px;
    width: 900px;
    height: 514px;
    overflow: hidden;
    box-shadow: 0 10px 30px rgba(0,0,0,0.12);
  }
  .card--front { top: 60px; background: var(--navy); }
  .card--back { top: 626px; background: var(--white); }

  .front__band {
    position: absolute;
    left: 0; right: 0;
    top: 430px;
    height: 26px;
    background: var(--green);
  }
  .brand {
    display: flex;
    align-items: center;
    gap: 18px;
    color: var(--green);
    font-weight: 600;
    letter-spacing: 0.12em;
    text-transform: uppercase;
  }
  .brand__mark { background: var(--green); flex: none; }
  .card--front .brand {
    position: absolute;
    left: 0; right: 0;
    top: 190px;
    justify-content: center;
    font-size: 40px;
  }
  .card--front .brand__mark { width: 44px; height: 44px; }

  .back__panel {
    position: absolute;
    left: 0; top: 0; bottom: 0;
    width: 400px;
    background: var(--navy);
    display: flex;
    flex-direction: column;
    justify-content: center;
    align-items: center;
    gap: 16px;
  }
  .card--back .brand { font-size: 22px; gap: 12px; }
  .card--back .brand__mark { width: 26px; height: 26px; }
  .tagline {
    color: var(--white);
    font-size: 19px;
    font-weight: 400;
  }

  .back__info {
    position: absolute;
    left: 450px; top: 60px;
    right: 30px;
  }
  .person__name {
    color: var(--green);
    font-size: 36px;
    font-weight: 300;
    line-height: 1.1;
    white-space: nowrap;
  }
  .person__name strong { font-weight: 700; }
  .person__name .credential { font-size: 24px; font-weight: 600; }
  .person__title {
    color: var(--navy);
    font-size: 17px;
    font-weight: 700;
    margin-top: 4px;
  }
  .contacts {
    list-style: none;
    margin-top: 40px;
    color: var(--ink);
    font-size: 17px;
    line-height: 1.55;
  }
  .contacts li { display: flex; align-items: flex-start; gap: 14px; }
  .contacts svg { width: 16px; height: 16px; margin-top: 6px; flex: none; fill: var(--green); }
  .contacts .gap { margin-top: 14px; }
</style>
</head>
<body>

<section class="card card--front" aria-label="Card front">
  <div class="brand"><span class="brand__mark"></span>Ledgerline Partners</div>
  <div class="front__band"></div>
</section>

<section class="card card--back" aria-label="Card back">
  <div class="back__panel">
    <div class="brand"><span class="brand__mark"></span>Ledgerline Partners</div>
    <p class="tagline">The Future of Investing</p>
  </div>

  <div class="back__info">
    <h1 class="person__name">Daniel <strong>Okafor</strong>, <span class="credential">CFA</span></h1>
    <p class="person__title">President</p>

    <ul class="contacts">
      <li>
        <svg viewBox="0 0 16 16"><path d="M3.5 1l3 3-1.6 1.8c.9 2 2.4 3.5 4.3 4.3L11 8.5l3 3-1.8 2.5C6.5 14 2 9.5 2 3.2z"/></svg>
        904-555-0142
      </li>
      <li>
        <svg viewBox="0 0 16 16"><path d="M4 0h8a1 1 0 0 1 1 1v14a1 1 0 0 1-1 1H4a1 1 0 0 1-1-1V1a1 1 0 0 1 1-1zm1 2v10h6V2zm3 11a1 1 0 1 0 0 2 1 1 0 0 0 0-2z"/></svg>
        585-555-0187
      </li>
      <li class="gap">
        <svg viewBox="0 0 16 16"><path d="M0 3h16v10H0zm1.5 1.5L8 9l6.5-4.5V4h-13z"/></svg>
        dokafor@ledgerline-partners.com
      </li>
      <li>
        <svg viewBox="0 0 16 16"><path d="M8 0a8 8 0 1 0 0 16A8 8 0 0 0 8 0zm-1 1.6V7H3.2A5 5 0 0 1 7 1.6zM9 1.6A5 5 0 0 1 12.8 7H9zM3.2 9H7v5.4A5 5 0 0 1 3.2 9zM9 9h3.8A5 5 0 0 1 9 14.4z"/></svg>
        www.ledgerline-partners.com
      </li>
      <li class="gap">
        <svg viewBox="0 0 16 16"><path d="M8 0a5.5 5.5 0 0 0-5.5 5.5C2.5 10 8 16 8 16s5.5-6 5.5-10.5A5.5 5.5 0 0 0 8 0zm0 7.5a2 2 0 1 1 0-4 2 2 0 0 1 0 4z"/></svg>
        <span>240 Harbor View Dr. Suite #210,<br>Seabrook Cove, FL 32099</span>
      </li>
    </ul>
  </div>
</section>

</body>
</html>
```